Business Card Design

We just need these details on one side of card and logo on the other.

Industry/Entity Type

Business

Contact Information for Business Card

Lisel Pardoe | Artist
118 Coldwell Street
Ashby Vale Vic 3188
# 0412 978 205 | 03 9187 2604
lisel@liselpardoe.com
liselsnook.com.au

```html
<!DOCTYPE html>
<html lang="en">
<head>
<meta charset="UTF-8">
<title>Lisel Pardoe — Business Card</title>
<link rel="stylesheet" href="https://fonts.googleapis.com/css2?family=Cinzel:wght@400&family=Open+Sans:wght@300;400&display=swap">
<style>
  :root {
    --backdrop: #e9e7e4;
    --card-black: #0d0d0d;
    --card-white: #f4f4f3;
    --ink-grey: #5a5a5a;
    --ink-dark: #2b2b2b;
    --ink-white: #f2f2f2;
  }
  * { margin: 0; padding: 0; box-sizing: border-box; }
  html, body {
    width: 1200px;
    height: 900px;
    overflow: hidden;
    background: var(--backdrop);
  }
  .canvas {
    width: 1200px;
    height: 900px;
    display: flex;
    align-items: center;
    justify-content: center;
    gap: 40px;
  }
  .card {
    width: 540px;
    height: 330px;
    position: relative;
    box-shadow: 0 6px 18px rgba(0,0,0,0.18);
    overflow: hidden;
  }

  /* Logo side */
  .card-front {
    background: var(--card-black);
    display: flex;
    flex-direction: column;
    align-items: center;
    justify-content: center;
  }
  .brand-name {
    font-family: "Open Sans", sans-serif;
    font-weight: 300;
    font-size: 46px;
    letter-spacing: 1px;
    color: var(--ink-white);
    line-height: 1.1;
  }
  .brand-tagline {
    margin-top: 8px;
    font-family: "Open Sans", sans-serif;
    font-weight: 300;
    font-size: 10px;
    letter-spacing: 3px;
    color: var(--ink-white);
  }

  /* Contact side */
  .card-back {
    background: var(--card-white);
  }
  .web-band {
    position: absolute;
    left: 0;
    bottom: 0;
    width: 100%;
    height: 40px;
    background: var(--card-black);
    display: flex;
    align-items: center;
    padding-left: 190px;
  }
  .web-address {
    white-space: nowrap;
    font-family: "Open Sans", sans-serif;
    font-weight: 400;
    font-size: 14px;
    letter-spacing: 1px;
    color: var(--ink-white);
  }
  .contact {
    position: absolute;
    left: 40px;
    top: 74px;
    right: 30px;
  }
  .contact-name {
    font-family: "Cinzel", serif;
    font-weight: 400;
    font-size: 19px;
    letter-spacing: 1.5px;
    color: var(--ink-dark);
    margin-left: 150px;
    margin-bottom: 14px;
  }
  .contact-lines {
    list-style: none;
    font-family: "Open Sans", sans-serif;
    font-weight: 400;
    font-size: 14px;
    line-height: 1.55;
    color: var(--ink-grey);
    white-space: nowrap;
  }
  .contact-lines .indent { padding-left: 62px; }
</style>
</head>
<body>
  <main class="canvas">
    <section class="card card-front" aria-label="Card front">
      <span class="brand-name">Lisel's Nook</span>
      <span class="brand-tagline">STUDIO · CAFE · GALLERY</span>
    </section>

    <section class="card card-back" aria-label="Card back">
      <div class="contact">
        <h1 class="contact-name">LISEL PARDOE</h1>
        <ul class="contact-lines">
          <li>Artist 118 Coldwell Street Ashby Vale Vic 3188</li>
          <li class="indent">0412 978 205</li>
          <li class="indent">03 9187 2604</li>
          <li class="indent">lisel@liselpardoe.com</li>
        </ul>
      </div>
      <div class="web-band">
        <span class="web-address">liselsnook.com.au</span>
      </div>
    </section>
  </main>
</body>
</html>
```